Q9 Clinic business card design

It is a doctor's business card. It will include both English and Chinese information ( will be provided). The design should look professional. It is an obstetrics and gynaecology clinic.

Target Market(s)

Hong Kong private medical market_adult females

Contact Information for Business Card

as the information provided_color coordination with the logo color

Font styles to use
Sans Serif

Colors

Designer to choose colors to be used in the design.

Requirements
Must have
• Logo.
• dr's name, credentials, address, telephone, fax no,

```html
<!DOCTYPE html>
<html lang="en">
<head>
<meta charset="utf-8">
<title>Q9 Clinic business card</title>
<link href="https://fonts.googleapis.com/css2?family=Open+Sans:wght@400;600;700&family=Noto+Sans+TC:wght@500;700&family=Noto+Serif+TC:wght@400&display=swap" rel="stylesheet">
<style>
  :root {
    --backdrop: #2b2b2d;
    --card-white: #f7f7f7;
    --clinic-blue: #1a5fa8;
    --clinic-blue-deep: #0f4e95;
    --clinic-green: #6fb82e;
    --ink: #3a3a3a;
    --muted: #7a7a7a;
    --rule: #9a9a9a;
  }
  * { box-sizing: border-box; margin: 0; padding: 0; }
  html, body { width: 1200px; height: 900px; overflow: hidden; }
  body {
    background: var(--backdrop);
    font-family: "Open Sans", sans-serif;
    display: flex; align-items: center; justify-content: center; gap: 70px;
  }
  .card {
    width: 360px; height: 600px; border-radius: 26px; overflow: hidden;
    position: relative; background: var(--card-white);
  }
  .brand { padding: 46px 0 0 40px; }
  .brand-name {
    font-family: "Open Sans", sans-serif; font-weight: 700; font-size: 44px;
    color: var(--clinic-blue); line-height: 1; letter-spacing: 0.5px;
  }
  .brand-tagline {
    margin-top: 6px; font-size: 11.5px; font-weight: 600; letter-spacing: 2px;
    color: var(--muted);
  }
  /* front (Chinese) card */
  .card-front .swoosh { position: absolute; left: 0; top: 118px; width: 360px; height: 90px; }
  .card-front .panel {
    position: absolute; left: 0; top: 170px; right: 0; bottom: 0;
    background: linear-gradient(180deg, var(--clinic-blue) 0%, var(--clinic-blue-deep) 100%);
    color: #fff; padding: 30px 36px 0 36px;
  }
  .zh-name { font-family: "Noto Sans TC", sans-serif; font-weight: 700; font-size: 19px; line-height: 1.4; margin-bottom: 6px; }
  .zh-credentials { font-family: "Noto Sans TC", sans-serif; font-weight: 500; font-size: 15px; line-height: 1.42; }
  .contact-list { list-style: none; margin-top: 16px; }
  .contact-list li { display: flex; align-items: center; gap: 12px; font-size: 16px; line-height: 1.55; }
  .contact-list svg { width: 14px; height: 14px; flex: none; }
  .panel .rule { border-top: 1px solid rgba(255,255,255,0.6); margin: 12px 0 14px; }
  .zh-address { font-family: "Noto Serif TC", serif; font-size: 16px; line-height: 1.4; color: #dfe9f5; margin-bottom: 12px; }
  /* back (English) card */
  .card-back .details { padding: 56px 36px 0 40px; }
  .doctor-name { font-weight: 700; font-size: 16px; color: var(--clinic-blue); }
  .credentials { font-weight: 700; font-size: 16px; color: var(--clinic-green); line-height: 1.3; }
  .card-back .contact-list li { color: var(--ink); }
  .card-back .rule { border-top: 1px solid var(--rule); margin: 18px 0 22px; }
  .en-address { font-size: 12.5px; color: var(--ink); line-height: 1.45; margin-bottom: 18px; }
</style>
</head>
<body>

<article class="card card-front" lang="zh-Hant">
  <header class="brand">
    <div class="brand-name">Q9 Clinic</div>
    <div class="brand-tagline">OBSTETRICS . GYNAECOLOGY</div>
  </header>
  <svg class="swoosh" viewBox="0 0 360 90" preserveAspectRatio="none" aria-hidden="true">
    <path d="M0 40 C120 20 250 10 360 2 L360 90 L0 90 Z" fill="var(--clinic-blue)"/>
    <path d="M0 44 C120 26 250 16 360 10 L360 24 C250 28 120 40 0 58 Z" fill="var(--clinic-green)"/>
    <path d="M0 58 C120 40 250 28 360 24 L360 30 C250 36 120 48 0 64 Z" fill="#ffffff"/>
  </svg>
  <section class="panel">
    <h1 class="zh-name">林穎熙醫生</h1>
    <p class="zh-credentials">東港大學內外全科醫學士<br>東港大學醫學碩士<br>太平洋醫學會院士(婦產科)<br>亞洲婦產科學會榮授院士<br>國際婦女健康醫學院院士</p>
    <ul class="contact-list">
      <li><svg viewBox="0 0 16 16"><path d="M3 5c0-2 2-2 5-2s5 0 5 2l-2 1-1-1H6L5 6z M4 8h8l1 4H3z" fill="#fff"/></svg>5555 555 555</li>
      <li><svg viewBox="0 0 16 16"><rect x="4" y="1" width="8" height="4" fill="#fff"/><rect x="2" y="6" width="12" height="6" rx="1" fill="#fff"/><rect x="4" y="10" width="8" height="5" fill="#fff" stroke="var(--clinic-blue)" stroke-width="1"/></svg>8888 888 888</li>
      <li><svg viewBox="0 0 16 16"><circle cx="8" cy="8" r="7" fill="var(--clinic-green)"/></svg>3333 333 333</li>
    </ul>
    <div class="rule"></div>
    <p class="zh-address">沙田火炭樂山路18號<br>海景廣場8樓805室</p>
    <p class="zh-address">尖沙咀廣東道88號<br>嘉峰中心B座6樓612室</p>
  </section>
</article>

<article class="card card-back" lang="en">
  <header class="brand">
    <div class="brand-name">Q9 Clinic</div>
    <div class="brand-tagline">OBSTETRICS . GYNAECOLOGY</div>
  </header>
  <section class="details">
    <h1 class="doctor-name">Dr Lam Wing Hei, Vincent</h1>
    <p class="credentials">MBBS, MMed, FEAMA(O&amp;G),<br>FPCWH, FIAWM</p>
    <ul class="contact-list">
      <li><svg viewBox="0 0 16 16"><path d="M3 5c0-2 2-2 5-2s5 0 5 2l-2 1-1-1H6L5 6z M4 8h8l1 4H3z" fill="var(--clinic-blue)"/></svg>5555 555 555</li>
      <li><svg viewBox="0 0 16 16"><rect x="4" y="1" width="8" height="4" fill="var(--clinic-blue)"/><rect x="2" y="6" width="12" height="6" rx="1" fill="var(--clinic-blue)"/><rect x="4" y="10" width="8" height="5" fill="var(--clinic-blue)" stroke="#fff" stroke-width="1"/></svg>8888 888 888</li>
      <li><svg viewBox="0 0 16 16"><circle cx="8" cy="8" r="7" fill="var(--clinic-green)"/></svg>3333 333 333</li>
    </ul>
    <div class="rule"></div>
    <p class="en-address">Unit 805, 8<sup>th</sup> floor, Harbourview Plaza,<br>18 Lok Shan Road, Fo Tan, Shatin,<br>New Territories, HONG KONG</p>
    <p class="en-address">Unit 612, 6<sup>th</sup> floor, Tower B, Crestline Centre,<br>88 Canton Road, Tsimshatsui, Kowloon,<br>HONG KONG</p>
  </section>
</article>

</body>
</html>
```